Album art for soul / electronic band

Album art for a singer / producer duo. Art should be similar to the copper lantern album art and be consistent with the color scheme in the attached band photo. The name of the album is corvelha (portuguese for delicate). Please do not include the photo in your design. Design should center around water.

Target Market(s)

Gen X / Millenial soul music fans

Industry/Entity Type

music

Font styles to use
Sans Serif

Requirements
Must have
• Clean modern look, photo or artwork.
Nice to have
• It should look like album art from groups in the same genre such as the Copper Lantern, Brasskite, K. Dunmore, Orrin Vale
Should not have
• band photo, musical notes, any music iconography

```html
<!DOCTYPE html>
<html lang="en">
<head>
<meta charset="utf-8">
<title>Corvelha — Valen Oro</title>
<link rel="stylesheet" href="https://fonts.googleapis.com/css2?family=Josefin+Sans:wght@200&family=Montserrat:wght@600&display=swap">
<style>
  :root {
    --sky-pale: #e3f2fd;
    --sky-light: #b9e3fd;
    --sky-mid: #8fd2fb;
    --ink-blue: #4a9cf0;
    --ink-deep: #2a78e0;
    --type-navy: #1d4a8a;
  }
  html, body {
    margin: 0;
    padding: 0;
    overflow: hidden;
    background: var(--sky-pale);
  }
  .album-cover {
    position: relative;
    width: 1197px;
    height: 1200px;
    overflow: hidden;
  }
  .watercolor-field {
    position: absolute;
    inset: 0;
    background:
      radial-gradient(ellipse 45% 18% at 62% 14%, rgba(42,120,224,0.55), transparent 70%),
      radial-gradient(ellipse 20% 25% at 92% 30%, rgba(58,135,235,0.45), transparent 70%),
      radial-gradient(ellipse 30% 20% at 15% 12%, rgba(180,225,253,0.8), transparent 70%),
      radial-gradient(ellipse 40% 30% at 55% 35%, rgba(200,228,252,0.7), transparent 70%),
      radial-gradient(ellipse 50% 40% at 40% 75%, rgba(170,222,253,0.8), transparent 70%),
      radial-gradient(ellipse 35% 35% at 85% 80%, rgba(225,240,254,0.9), transparent 70%),
      linear-gradient(170deg, var(--sky-mid) 0%, var(--sky-light) 50%, var(--sky-pale) 100%);
  }
  .album-title {
    position: absolute;
    left: 0;
    right: 0;
    top: 936px;
    margin: 0;
    text-align: center;
    font-family: "Josefin Sans", sans-serif;
    font-weight: 200;
    font-size: 68px;
    line-height: 1;
    letter-spacing: 0.62em;
    text-indent: 0.62em;
    color: var(--type-navy);
  }
  .artist-name {
    position: absolute;
    left: 0;
    right: 0;
    top: 1053px;
    margin: 0;
    text-align: center;
    font-family: "Montserrat", sans-serif;
    font-weight: 600;
    font-size: 23px;
    line-height: 1;
    letter-spacing: 0.3em;
    text-indent: 0.3em;
    color: var(--type-navy);
  }
</style>
</head>
<body>
  <main class="album-cover">
    <div class="watercolor-field" role="img" aria-label="Abstract blue watercolour ink wash evoking flowing water, deeper blue pooled ink along the upper area"></div>
    <h1 class="album-title">CORVELHA</h1>
    <p class="artist-name">VALEN ORO</p>
  </main>
</body>
</html>
```